RTV Electrical – Fridge Magnet & Letterbox Leaflet

Overview
We are a local electrical contractor based in Gooseberry Hill in the Perth Hills (Western Australia).
We are looking for a designer to create:
1️⃣ A fridge magnet design
2️⃣ A matching letterbox leaflet (A6 or DL)
The goal is to create clean, professional marketing that feels local and trustworthy, not flashy advertising.
The designs must feel like a high-quality local trades business, appealing to homeowners in suburbs such as:
Kalamunda
Gooseberry Hill
Lesmurdie
Walliston
Pickering Brook
Design Style
The design should feel:
✔ Local
✔ Authentic
✔ Professional
✔ Trustworthy
✔ Clean and simple
NOT:
✖ Cheap advertising
✖ Overly flashy
✖ Busy or cluttered
Think premium local tradesman, not mass marketing.
Branding
Use our brand colours inspired by our van:
Primary colours
Navy Blue
White
Accent colour
Yellow / gold highlight
Design should match the look of our work van branding.
Images Provided
We will provide:
✔ Company logo
✔ Photo of our branded van in the Perth Hills
The van photo should be used in the leaflet design to reinforce our local presence.
Fridge Magnet Design
Size suggestion:
90mm x 55mm
Purpose:
Homeowners keep this magnet so they can easily call a trusted electrician.
Must include:
RTV Electrical Contracting
Local Perth Hills Electrician
Based in Gooseberry Hill
Phone number (large and clear)
📞 0491 726 054
Services:
• Fault finding
• Switchboard upgrades
• Lighting & power
• Ceiling fans
• Smoke alarm compliance
Also include:
⭐ 110+ Starfold Reviews
Website:
www.rtvelectrical.com.au
Design should be very simple and easy to read from across a kitchen.
Leaflet Design
Size options:
A6 or DL
Purpose:
Letterbox drop marketing in Perth Hills suburbs.
Front Side
Headline:
WE'RE WORKING IN YOUR AREA
Subtext:
Local electrician based in Gooseberry Hill
Include:
✔ Photo of our van
✔ RTV logo
✔ Key services
Services:
• Fault finding
• Switchboard upgrades
• Lighting & power
• Ceiling fans
• Smoke alarm compliance
Call to action:
📞 Call Marcus – 0491 726 054
⭐ 110+ Five-Star Starfold Reviews
Back Side
Headline:
Your Local Perth Hills Electrician
Servicing:
Kalamunda
Gooseberry Hill
Lesmurdie
Walliston
Pickering Brook
Short message:
Reliable electrical work across the Perth Hills.
Call Marcus
📞 0491 726 054
Website:
www.rtvelectrical.com.au
EC47286
Target Audience
Homeowners in the Perth Hills aged 35–70.
Many homes are older properties and often need electrical upgrades, repairs and safety work.
Design should appeal to homeowners who value reliability and local service.
Deliverables
Designers must provide:
✔ Print-ready files
✔ Editable source files
✔ High resolution files
For:
Fridge magnet
Leaflet front and back
Final Notes
This design should communicate:
✔ Trusted local electrician
✔ Established business
✔ Professional service
✔ Easy to contact
The goal is to create marketing people will keep, not throw away.

```html
<!DOCTYPE html>
<html lang="en">
<head>
<meta charset="utf-8">
<title>RTV Electrical – Fridge Magnet &amp; Letterbox Leaflet</title>
<link rel="stylesheet" href="https://fonts.googleapis.com/css2?family=Montserrat:wght@400;500;600;700;800&display=swap">
<style>
:root{
  --navy:#0d2360;
  --yellow:#f5c400;
  --grey:#6a6a6a;
  --band:#7a7a7a;
  --white:#ffffff;
  --sheet-top:#9aa8bd;
  --sheet-mid:#b3bfd0;
  --photo-a:#e7ebf1;
  --photo-b:#b9c4d4;
}
*{box-sizing:border-box;margin:0;padding:0}
html,body{width:881px;height:1200px;overflow:hidden}
body{
  font-family:"Montserrat",Arial,sans-serif;
  background:radial-gradient(ellipse at 50% 45%,var(--sheet-mid),var(--sheet-top) 70%);
  position:relative;
}
.sheet-label{
  position:absolute;color:var(--white);font-size:18px;font-weight:500;
  letter-spacing:2.6px;text-align:center;white-space:nowrap;transform:translateX(-50%);
}
.sheet-label b{font-weight:700}

/* Fridge magnet */
.magnet{position:absolute;left:247px;top:61px;width:387px;height:236px;background:var(--white);overflow:hidden}
.magnet__mark{position:absolute;left:8px;top:62px;width:88px;height:100px;background:var(--navy);
  display:flex;align-items:center;justify-content:center;text-align:center;
  color:var(--white);font-weight:700;font-size:14px;line-height:1.25}
.magnet__title{position:absolute;left:128px;top:18px;color:var(--navy);font-weight:800;font-size:22px;line-height:1.08;white-space:nowrap}
.magnet__bar{position:absolute;left:116px;top:74px;width:249px;height:31px;background:var(--navy);color:var(--white);
  font-weight:700;font-size:14.5px;line-height:31px;padding-left:12px;white-space:nowrap}
.magnet__phone{position:absolute;left:128px;top:111px;display:flex;align-items:center;gap:12px;color:var(--navy);font-weight:800;font-size:30px;white-space:nowrap}
.magnet__services{position:absolute;left:107px;top:150px;color:var(--grey);font-size:12px;font-weight:500;line-height:15.5px;white-space:nowrap}
.magnet__web{position:absolute;left:107px;top:199px;width:139px;height:20px;background:var(--navy);color:var(--white);
  font-size:10.5px;font-weight:700;display:flex;align-items:center;gap:7px;padding-left:9px;white-space:nowrap}
.magnet__count{position:absolute;left:252px;top:199px;width:51px;height:20px;border:1px solid var(--navy);
  color:var(--navy);font-size:14px;font-weight:600;text-align:center;line-height:18px}
.magnet__rating{position:absolute;left:308px;top:196px;color:var(--navy);font-size:12.5px;font-weight:700;line-height:1}
.magnet__rating small{display:block;font-size:6px;font-weight:600;color:var(--grey)}
.magnet__rating small span{color:var(--yellow)}

/* Leaflets */
.leaflet{position:absolute;top:347px;width:385px;height:821px;background:var(--white);overflow:hidden}
.leaflet--front{left:46px}
.leaflet--back{left:450px}
.photo{position:absolute;background:linear-gradient(160deg,var(--photo-a),var(--photo-b))}
.brand{position:absolute;left:96px;top:38px;display:flex;align-items:center;gap:14px}
.brand__square{width:51px;height:71px;background:var(--navy)}
.brand__name{color:var(--navy);font-size:19px;font-weight:500;line-height:1.15;border-bottom:1px solid var(--navy);white-space:nowrap}
.tag{position:absolute;border:1.5px solid var(--yellow);background:var(--white);color:var(--grey);font-weight:600;text-align:center;white-space:nowrap}
.headline{position:absolute;left:0;width:100%;text-align:center;color:var(--navy);font-weight:800;white-space:nowrap}
.rule{position:absolute;left:48px;top:220px;width:290px;height:1px;background:var(--grey)}
.sub{position:absolute;left:0;width:100%;text-align:center;white-space:nowrap}
.service-grid{position:absolute;display:grid;grid-template-columns:145px 145px;z-index:2}
.service{height:66px;display:flex;align-items:center;gap:7px;padding-left:11px;font-size:15px;letter-spacing:-.2px;line-height:1.15;font-weight:500;white-space:nowrap}
.service--dark{background:var(--navy);color:var(--white)}
.service--light{background:transparent;color:var(--grey)}
.service svg{flex:none}
.reviews{position:absolute;left:24px;top:544px;width:116px;z-index:3}
.reviews__count{height:44px;background:var(--yellow);color:var(--white);font-size:32px;font-weight:700;text-align:center;line-height:44px}
.reviews__label{height:50px;background:var(--white);border:1px solid var(--yellow);border-top:0;text-align:center;padding-top:6px;
  color:var(--navy);font-size:18px;font-weight:700;line-height:1.1}
.reviews__label small{display:block;font-size:9px;font-weight:600;color:var(--grey)}
.reviews__label small span{color:var(--yellow)}
.call-bar{position:absolute;left:0;bottom:0;width:100%;height:73px;background:var(--navy);color:var(--white);
  display:flex;align-items:center;justify-content:center;gap:10px;z-index:3}
.call-bar__who{font-size:16px;font-weight:600;padding-right:10px;border-right:1px solid var(--white);line-height:26px}
.call-bar__number{font-size:29px;font-weight:700}
.back-band{position:absolute;left:0;top:518px;width:100%;height:69px;background:var(--band);color:var(--white);
  font-size:15.5px;font-weight:600;line-height:1.2;padding:16px 0 0 51px;white-space:nowrap;z-index:1}
.back-band__text{position:relative;z-index:3}
.reach{position:absolute;left:37px;top:632px;color:var(--navy);font-size:13.5px;font-weight:700;z-index:3}
.web-box{position:absolute;left:22px;top:655px;width:200px;height:45px;border:1px solid var(--navy);background:var(--white);
  display:flex;align-items:center;gap:10px;padding-left:14px;color:var(--navy);font-size:14.5px;font-weight:500;white-space:nowrap;z-index:3}
</style>
</head>
<body>

<div class="sheet-label" style="left:440px;top:28px">FRIDGE MAGNET DESIGN</div>

<section class="magnet" aria-label="Fridge magnet">
  <div class="magnet__mark">RTV<br>Electrical</div>
  <h1 class="magnet__title">LOCAL PERTH HILLS<br>ELECTRICIAN</h1>
  <div class="magnet__bar">BASED IN GOOSEBERRY HILL</div>
  <div class="magnet__phone">
    <svg width="24" height="24" viewBox="0 0 24 24" aria-hidden="true"><path fill="#0d2360" d="M6.6 10.8a15.1 15.1 0 0 0 6.6 6.6l2.2-2.2c.3-.3.7-.4 1-.2 1.1.4 2.3.6 3.6.6.6 0 1 .4 1 1V20c0 .6-.4 1-1 1A17 17 0 0 1 3 4c0-.6.4-1 1-1h3.5c.6 0 1 .4 1 1 0 1.3.2 2.5.6 3.6.1.3 0 .7-.2 1z"/></svg>
    <span>0491 726 054</span>
  </div>
  <p class="magnet__services">Fault finding &nbsp;|&nbsp; Switchboard upgrades<br>| &nbsp;Lighting &amp; power &nbsp;|&nbsp; Ceiling fans &nbsp;|&nbsp; Smoke<br>alarm compliance</p>
  <div class="magnet__web">
    <svg width="9" height="9" viewBox="0 0 10 10" aria-hidden="true"><path fill="#fff" d="M10 0 0 4l4 2 2 4z"/></svg>
    rtvelectrical.com.au
  </div>
  <div class="magnet__count">110+</div>
  <div class="magnet__rating">Starfold<small>Reviews <span>★★★★★</span></small></div>
</section>

<div class="sheet-label" style="left:239px;top:316px">LETTERBOX LEAFLET <b>FRONT</b></div>
<div class="sheet-label" style="left:643px;top:316px">LETTERBOX LEAFLET <b>BACK</b></div>

<!-- Leaflet front -->
<section class="leaflet leaflet--front" aria-label="Letterbox leaflet front">
  <div class="brand">
    <div class="brand__square"></div>
    <div class="brand__name">RTV Electrical<br>Contracting</div>
  </div>
  <div class="photo" role="img" aria-label="Lightning bolt decoration" style="left:300px;top:95px;width:28px;height:70px;opacity:.45"></div>
  <div class="tag" style="left:88px;top:138px;width:210px;height:42px;font-size:22px;line-height:40px;transform:rotate(-4deg)">WE'RE WORKING</div>
  <h2 class="headline" style="top:176px;font-size:38px">IN YOUR AREA</h2>
  <div class="rule"></div>
  <p class="sub" style="top:233px;color:var(--grey);font-size:19px;font-weight:600">Local Electrician based in</p>
  <p class="sub" style="top:259px;color:var(--navy);font-size:21px;font-weight:600">Gooseberry Hill</p>

  <div class="photo" role="img" aria-label="Electrician in hard hat holding a toolbox of cable" style="left:200px;top:430px;width:160px;height:210px;border-radius:40px 40px 0 0"></div>
  <div class="photo" role="img" aria-label="Company work van parked in the Perth Hills" style="left:55px;top:580px;width:330px;height:168px;border-radius:60px 0 0 0;background:linear-gradient(160deg,#d9dfe8,#22356b 70%)"></div>

  <div class="service-grid" style="left:48px;top:312px">
    <div class="service service--dark"><svg width="14" height="14" viewBox="0 0 14 14" aria-hidden="true"><circle cx="5.5" cy="5.5" r="4" fill="none" stroke="#fff" stroke-width="1.6"/><path d="M8.5 8.5 13 13" stroke="#fff" stroke-width="1.8"/></svg>Fault Finding</div>
    <div class="service service--light"><svg width="12" height="14" viewBox="0 0 12 14" aria-hidden="true"><path fill="#0d2360" d="M6 1a4 4 0 0 0-4 4v4L1 11h10L10 9V5a4 4 0 0 0-4-4zM4.5 12a1.5 1.5 0 0 0 3 0z"/></svg>Smoke Alarm<br>Compliance</div>
    <div class="service service--light"><svg width="14" height="14" viewBox="0 0 14 14" aria-hidden="true"><circle cx="7" cy="7" r="5.5" fill="none" stroke="#0d2360" stroke-width="2.4" stroke-dasharray="2.5 1.8"/><circle cx="7" cy="7" r="2" fill="#0d2360"/></svg>Switchboard<br>Upgrades</div>
    <div class="service service--dark"><svg width="16" height="12" viewBox="0 0 16 12" aria-hidden="true"><path d="M8 0v5M1 6h14M8 6l-3 5M8 6l3 5" stroke="#fff" stroke-width="1.4" fill="none"/></svg>Ceiling Fans</div>
    <div class="service service--dark"><svg width="12" height="16" viewBox="0 0 12 16" aria-hidden="true"><path fill="#fff" d="M7 0 0 9h5l-1 7 8-10H7z"/></svg>Lighting<br>And Power</div>
  </div>

  <div class="reviews">
    <div class="reviews__count">110+</div>
    <div class="reviews__label">Starfold<small>Reviews <span>★★★★★</span></small></div>
  </div>

  <div class="call-bar"><span class="call-bar__who">Call Marcus</span><span class="call-bar__number">0491 726 054</span></div>
</section>

<!-- Leaflet back -->
<section class="leaflet leaflet--back" aria-label="Letterbox leaflet back">
  <p class="sub" style="top:58px;color:#555;font-size:23px;font-weight:500">YOUR LOCAL</p>
  <h2 class="headline" style="top:88px;font-size:42px;letter-spacing:-.5px">PERTH HILLS</h2>
  <div class="tag" style="left:60px;top:134px;width:264px;height:60px;font-size:33px;line-height:58px;color:#5e5e5e;font-weight:700;transform:rotate(-3deg);z-index:1">ELECTRICIAN</div>
  <div class="photo" role="img" aria-label="Lightning bolt decoration" style="left:312px;top:200px;width:22px;height:60px;opacity:.45"></div>
  <p class="sub" style="top:229px;color:var(--yellow);font-size:27px;font-weight:700">OUR SERVICES</p>

  <div class="service-grid" style="left:50px;top:288px">
    <div class="service service--dark"><svg width="14" height="14" viewBox="0 0 14 14" aria-hidden="true"><circle cx="5.5" cy="5.5" r="4" fill="none" stroke="#fff" stroke-width="1.6"/><path d="M8.5 8.5 13 13" stroke="#fff" stroke-width="1.8"/></svg>Fault Finding</div>
    <div class="service service--light"><svg width="12" height="14" viewBox="0 0 12 14" aria-hidden="true"><path fill="#0d2360" d="M6 1a4 4 0 0 0-4 4v4L1 11h10L10 9V5a4 4 0 0 0-4-4zM4.5 12a1.5 1.5 0 0 0 3 0z"/></svg>Smoke Alarm<br>Compliance</div>
    <div class="service service--light"><svg width="14" height="14" viewBox="0 0 14 14" aria-hidden="true"><circle cx="7" cy="7" r="5.5" fill="none" stroke="#0d2360" stroke-width="2.4" stroke-dasharray="2.5 1.8"/><circle cx="7" cy="7" r="2" fill="#0d2360"/></svg>Switchboard<br>Upgrades</div>
    <div class="service service--dark"><svg width="16" height="12" viewBox="0 0 16 12" aria-hidden="true"><path d="M8 0v5M1 6h14M8 6l-3 5M8 6l3 5" stroke="#fff" stroke-width="1.4" fill="none"/></svg>Ceiling Fans</div>
    <div class="service service--dark"><svg width="12" height="16" viewBox="0 0 12 16" aria-hidden="true"><path fill="#fff" d="M7 0 0 9h5l-1 7 8-10H7z"/></svg>Lighting<br>And Power</div>
  </div>

  <div class="back-band"><span class="back-band__text">Reliable Electrical Work<br>Across The Perth Hills.</span></div>
  <div class="photo" role="img" aria-label="Smiling electrician in hard hat and navy overalls holding cable and pliers" style="left:252px;top:477px;width:126px;height:280px;z-index:2;border-radius:50px 50px 0 0;background:linear-gradient(170deg,#f2d27a 0%,#2f4d78 35%,#1d3556 100%)"></div>
  <p class="reach">REACH US!</p>
  <div class="web-box">
    <svg width="11" height="11" viewBox="0 0 10 10" aria-hidden="true"><path fill="#0d2360" d="M10 0 0 4l4 2 2 4z"/></svg>
    rtvelectrical.com.au
  </div>

  <div class="call-bar" style="height:67px"><span class="call-bar__who">Call Marcus</span><span class="call-bar__number">0491 726 054</span></div>
</section>

</body>
</html>
```